Updated Package Design for FloraPeak

1. We have a package that we are manufacturing. It has been well recieved and everybody likes it.

2. We have a client in the EU who wants some design changes. Something more suited to their clientele. Young and hip, I am told. Basically this product will be sold as an accessory to Sports Water Bottles. So it will be hanging on clip strips next to the bottles.

3. Attached we have the current design w/ dimensions attached and the EU package idea as well.

4. What we want is a FRESH LOOK at the text and a HYBRID of the two. Look at the brief.

5. What we don't want to do is TOTALLY change everything (because I'll have to change EVERYTHING downstream attached to it and I don't want to do that)

6. Attached files are a version of the brief w/ images. front and back AI files of the current package.

View product online:

http://theflorapeak-example.com/

Target Market(s)

Industry/Entity Type

Water Treatment

Font styles to use
Sans Serif

Requirements
Must have
• Clean, fresh, green, healthy and hip.
Nice to have
• 4. What we want is a FRESH LOOK at the text and a HYBRID of the two. Look at the brief.
Should not have
• 5. What we don't want to do is TOTALLY change everything (because I'll have to change EVERYTHING downstream attached to it and I don't want to do that)

```html
<!DOCTYPE html>
<html lang="en">
<head>
<meta charset="utf-8">
<title>FloraPeak – Package Front</title>
<link href="https://fonts.googleapis.com/css2?family=Open+Sans:wght@400;700;800&display=swap" rel="stylesheet">
<style>
  :root {
    --backdrop: #808080;
    --pack-white: #ffffff;
    --cap-orange: #f26a21;
    --cap-orange-dark: #d9541a;
    --brand-grey: #4a4f55;
    --brand-dot: #9bb04a;
    --water-light: #e4f1fb;
    --water-mid: #8cc3ea;
    --badge-red: #e2412b;
    --badge-red-dark: #c3281a;
    --text-blue: #1d63b0;
    --wave-blue: #1a5fb4;
    --wave-light: #4f97d8;
  }
  html, body {
    margin: 0;
    padding: 0;
    overflow: hidden;
  }
  body {
    width: 1200px;
    height: 2708px;
    background: var(--backdrop);
    font-family: "Open Sans", Arial, sans-serif;
  }
  .package {
    position: relative;
    width: 1200px;
    height: 2708px;
  }
  .package-outline {
    position: absolute;
    inset: 0;
  }
  .cap-label {
    position: absolute;
    top: 262px;
    font-size: 17px;
    font-weight: 700;
    color: var(--pack-white);
    letter-spacing: 1px;
  }
  .cap-label--tear { left: 500px; }
  .cap-label--reuse { left: 640px; }
  .brand {
    position: absolute;
    top: 585px;
    left: 0;
    width: 1200px;
    display: flex;
    justify-content: center;
    align-items: center;
    gap: 26px;
  }
  .brand-dot {
    width: 80px;
    height: 80px;
    border-radius: 50%;
    background: var(--brand-dot);
  }
  .brand-name {
    font-size: 104px;
    font-weight: 700;
    color: var(--brand-grey);
    letter-spacing: -2px;
    line-height: 1;
  }
  .splash {
    position: absolute;
    top: 760px;
    left: 80px;
    width: 1040px;
    height: 190px;
    background: linear-gradient(180deg, rgba(255,255,255,0) 0%, var(--water-light) 35%, var(--water-mid) 60%, var(--water-light) 80%, rgba(255,255,255,0) 100%);
  }
  .badge {
    position: absolute;
    top: 862px;
    left: 382px;
    width: 460px;
    height: 318px;
    border-radius: 70px;
    background: radial-gradient(ellipse at 50% 30%, var(--badge-red) 55%, var(--badge-red-dark) 100%);
    color: var(--pack-white);
    text-align: center;
    font-weight: 800;
    display: flex;
    flex-direction: column;
    justify-content: center;
    line-height: 1;
  }
  .badge-line--big { font-size: 108px; letter-spacing: 2px; }
  .badge-line--spaced { font-size: 76px; letter-spacing: 34px; margin: 8px 0 10px 34px; }
  .tagline {
    position: absolute;
    top: 2180px;
    left: 0;
    width: 1200px;
    text-align: center;
    font-size: 66px;
    font-weight: 700;
    color: var(--text-blue);
    line-height: 1.25;
    margin: 0;
  }
</style>
</head>
<body>
<main class="package">
  <svg class="package-outline" width="1200" height="2708" viewBox="0 0 1200 2708" aria-hidden="true">
    <path fill="var(--pack-white)" d="M240 10 H960 Q1020 10 1020 70 V250 C1020 320 830 320 830 400 C830 520 1110 520 1110 700 C1110 1000 1080 1200 1080 1400 C1080 1700 1120 1900 1120 2200 V2600 Q1120 2690 1030 2690 H170 Q80 2690 80 2600 V2200 C80 1900 120 1700 120 1400 C120 1200 90 1000 90 700 C90 520 370 520 370 400 C370 320 180 320 180 250 V70 Q180 10 240 10 Z"/>
    <circle cx="600" cy="52" r="26" fill="var(--backdrop)"/>
    <!-- cap -->
    <path fill="var(--cap-orange)" d="M410 340 V210 Q410 180 440 180 H760 Q790 180 790 210 V340 Z"/>
    <rect x="410" y="320" width="380" height="20" fill="var(--cap-orange-dark)"/>
    <!-- zipper -->
    <line x1="380" y1="300" x2="820" y2="300" stroke="#333" stroke-width="6" stroke-dasharray="4 4"/>
    <rect x="372" y="290" width="26" height="20" rx="4" fill="none" stroke="#333" stroke-width="5"/>
    <!-- waves -->
    <path d="M230 2140 C480 2110 720 2110 970 2140" fill="none" stroke="var(--wave-blue)" stroke-width="14" stroke-linecap="round"/>
    <path d="M230 2410 C480 2440 720 2440 990 2400" fill="none" stroke="var(--wave-light)" stroke-width="10" stroke-linecap="round"/>
    <!-- recycle icon -->
    <g fill="none" stroke="var(--wave-blue)" stroke-width="12" stroke-linecap="round" stroke-linejoin="round">
      <path d="M600 2470 L640 2540"/>
      <path d="M625 2545 L560 2545"/>
      <path d="M548 2530 L585 2468"/>
      <path d="M628 2524 L641 2542 L620 2552"/>
      <path d="M573 2533 L560 2545 L575 2560"/>
      <path d="M584 2490 L586 2468 L606 2475"/>
    </g>
  </svg>

  <span class="cap-label cap-label--tear">TEAR HERE</span>
  <span class="cap-label cap-label--reuse">REUSABLE BAG</span>

  <div class="brand">
    <span class="brand-dot"></span>
    <span class="brand-name">FloraPeak</span>
  </div>

  <div class="splash" role="img" aria-label="Splash of clear water with bubbles"></div>

  <div class="badge">
    <span class="badge-line--big">INSERT</span>
    <span class="badge-line--spaced">SWIRL</span>
    <span class="badge-line--big">DRINK</span>
  </div>

  <p class="tagline">Portable water pufier<br>for your tap water</p>
</main>
</body>
</html>
```